Online Music Gear Store needs Business Cards

We need BC designs for our e-commerce for meetings and networking
we are an Online Store and we sell Audio and Music Equipment and Gear
we also provide EVENTUAL Audio and Music Production services but our core service is the Online Store: Selling Premium Brands

we are based in Tijuana and San Diego CA.
our brand/name is: Vellmoor

our name comes from the early tape machines that the Corvanes and many other early day artist used to record with to do their magnificent masterpieces.

Now in 2014 we can have Amazing Studio-Quality Multitrack sessions with a few pieces of Gear and an Slatepod... For example, you can only have your Pocketline and an Brisa Tandem to start recording using Loft Deck for Quorix.

If the best bands from the early days had to use million dollar recording studios with very expensive gear such as 4-track tape machines... now you can achieve better sounding results in your bedroom, using the gear we sell.

Thats what we try to Communicate with the Name:

That you... a young musician can start doing multitrack sessions using the Best Gear with the Latest Technology and compatible with Trelons, Quorix devices:

Example of the Premium Brands we sell are:
Brisa, ZQ Mediaworks

we want to communicate (even if we are an ecommerce and a startup) that we are Serious, and Very Elegant, Sophisticated and Minimal.

that we provide Complete solutions, the best gear... the best brands... that we also do our productions with the best gear, best brands and very important we are Pomeroy ONLY, Trelons Only

examples of the brands we sell are Kolbrandt, Brisa, ZQ Mediaworks, Rolf Ingham Instruments, Arc 9. Our focus is Music Technology.
we also use Cadence Max Q.

Our favorite colors are black, white, grey, silver, orange, blue, green, maybe bit of yellow.

No need to use all of them but you can combine. At the end you can use Color Theory to achieve assertive communication.

Target Market(s)

CEO's, VP's, VC's, Sales People, High Class executives...
Purchasing Departments, and Corporations.

Industry/Entity Type

E-Commerce

Requirements
Must have
• Should include:

1. Logo
2. website,
3. Managing Director Info:
4. Minimal and Elegant/Upper Class

feel free to suggest ideas, feel free to play around with logo and fonts as well... since we are not 100% happy with our logo...

must also show that we are Pomeroy and Trelon only in a way without being obvious or without showing Pomeroy Logo

we need to have at the end of the project the .AI
.PSD and any related designed file to edit in the future, logo, numbers, etc...

my info:

Tomas Emil Varga-Lindqvist
Vellmoor | Valdera, Porto Lume, Santa Brisa,
Chatterbox | Peeplo | Zenbo+ | Clipwall | Snapframe ???? (what do you thing about this links ???) too much ???
Mobile: +5219987350418 | 0115219987350418
USA Number: 1-800-572-9183
VuCall & QuickNote: studio@vellmoor-example.mx
Talkwave: studiovellmoormx
Should not have
• it shouldn't use our real address, but should imply that we are in Mexico City, in Tijuana and San Diego CA.

Should not use the Pomeroy Logo (even if we are Pomeroy only)

should not have Robotix or PC/Panelix related designs.

```html
<!DOCTYPE html>
<html lang="en">
<head>
<meta charset="utf-8">
<title>Vellmoor Business Card</title>
<link rel="stylesheet" href="https://fonts.googleapis.com/css2?family=Jura:wght@400;600&display=swap">
<style>
  :root {
    --stage: #2b2b2b;
    --card-light-top: #ffffff;
    --card-light-bottom: #dcdcdc;
    --card-dark: #050505;
    --ink-dark: #3a3a3a;
    --ink-mid: #6b6b6b;
    --rule: #9a9a9a;
    --silver: #c9c9c9;
    --white: #ffffff;
    --icon-bg: #1c1c1c;
  }
  * { box-sizing: border-box; margin: 0; padding: 0; }
  html, body { width: 1200px; height: 900px; overflow: hidden; }
  body {
    background: var(--stage);
    font-family: "Jura", sans-serif;
    position: relative;
  }
  .card {
    position: absolute;
    top: 300px;
    width: 520px;
    height: 300px;
    box-shadow: 0 6px 18px rgba(0,0,0,0.45);
  }
  .card-front {
    left: 50px;
    background: linear-gradient(180deg, var(--card-light-top) 0%, var(--card-light-bottom) 100%);
    color: var(--ink-dark);
  }
  .card-back {
    left: 630px;
    background: var(--card-dark);
    border: 1px solid #3a3a3a;
    color: var(--white);
  }

  .brand {
    position: absolute;
    display: flex;
    align-items: center;
    gap: 10px;
    font-weight: 600;
    letter-spacing: 0.5px;
  }
  .brand-dot {
    width: 18px; height: 18px; border-radius: 50%;
    background: currentColor;
  }
  .card-front .brand {
    left: 0; width: 250px; top: 122px;
    justify-content: center;
    font-size: 40px;
    color: var(--ink-dark);
  }
  .card-back .brand {
    left: 0; width: 100%; top: 95px;
    justify-content: center;
    font-size: 52px;
    color: var(--silver);
  }

  .divider-vertical {
    position: absolute;
    left: 252px; top: 18px;
    width: 2px; height: 264px;
    background: linear-gradient(180deg, #b5b5b5, #7a7a7a);
  }

  .person {
    position: absolute;
    left: 268px; right: 22px; top: 24px;
  }
  .person-name {
    font-size: 17px;
    font-weight: 600;
    color: var(--ink-dark);
    white-space: nowrap;
  }
  .person-role {
    margin-top: 4px;
    padding-top: 5px;
    border-top: 1px solid var(--rule);
    text-align: right;
    font-size: 13px;
    color: var(--ink-mid);
  }

  .contacts {
    position: absolute;
    right: 22px; top: 122px;
    list-style: none;
    text-align: right;
  }
  .contacts li {
    display: flex;
    justify-content: flex-end;
    align-items: center;
    gap: 8px;
    font-size: 11.5px;
    color: var(--ink-dark);
    height: 25px;
    white-space: nowrap;
  }
  .contacts li:first-child { font-size: 12.5px; }
  .icon {
    width: 15px; height: 15px; flex: none;
  }

  .card-back .divider-horizontal {
    position: absolute;
    left: 0; right: 0; top: 238px;
    height: 2px;
    background: linear-gradient(90deg, #444, #8a8a8a 50%, #444);
  }
  .website {
    position: absolute;
    left: 0; right: 0; top: 252px;
    text-align: center;
    font-size: 15px;
    color: var(--white);
    letter-spacing: 0.3px;
  }
</style>
</head>
<body>

  <section class="card card-front" aria-label="Business card front">
    <div class="brand"><span class="brand-dot"></span>Vellmoor</div>
    <div class="divider-vertical"></div>

    <div class="person">
      <p class="person-name">Tomas Emil Varga-Lindqvist</p>
      <p class="person-role">Managing Director</p>
    </div>

    <ul class="contacts">
      <li>Valdera, Porto Lume, Santa Brisa
        <svg class="icon" viewBox="0 0 16 16" aria-hidden="true"><circle cx="8" cy="8" r="8" fill="var(--icon-bg)"/><path d="M8 3.5a2.8 2.8 0 0 0-2.8 2.8C5.2 8.5 8 12.5 8 12.5s2.8-4 2.8-6.2A2.8 2.8 0 0 0 8 3.5z" fill="#fff"/><circle cx="8" cy="6.3" r="1" fill="var(--icon-bg)"/></svg>
      </li>
      <li>5219987350418 | 0115219987350418
        <svg class="icon" viewBox="0 0 16 16" aria-hidden="true"><circle cx="8" cy="8" r="8" fill="var(--icon-bg)"/><rect x="5.3" y="3.5" width="5.4" height="9" rx="1" fill="#fff"/><rect x="6.2" y="4.6" width="3.6" height="5.8" fill="var(--icon-bg)"/></svg>
      </li>
      <li>USA Number: 1-800-572-9183
        <svg class="icon" viewBox="0 0 16 16" aria-hidden="true"><circle cx="8" cy="8" r="8" fill="var(--icon-bg)"/><path d="M5.2 4.2l1.5-.4.9 2-1 .8a5 5 0 0 0 2.8 2.8l.8-1 2 .9-.4 1.5c-3.6.2-6.8-3-6.6-6.6z" fill="#fff"/></svg>
      </li>
      <li>studiovellmoormx
        <svg class="icon" viewBox="0 0 16 16" aria-hidden="true"><circle cx="8" cy="8" r="8" fill="var(--icon-bg)"/><path d="M4 5h8v5H7.5L5.5 12v-2H4z" fill="#fff"/></svg>
      </li>
      <li>studio@vellmoor-example.mx
        <svg class="icon" viewBox="0 0 16 16" aria-hidden="true"><circle cx="8" cy="8" r="8" fill="var(--icon-bg)"/><rect x="4" y="5" width="8" height="6" fill="#fff"/><path d="M4 5l4 3.2L12 5" fill="none" stroke="var(--icon-bg)" stroke-width="0.9"/></svg>
      </li>
    </ul>
  </section>

  <section class="card card-back" aria-label="Business card back">
    <div class="brand"><span class="brand-dot"></span>Vellmoor</div>
    <div class="divider-horizontal"></div>
    <p class="website">www.vellmoor-example.mx</p>
  </section>

</body>
</html>
```